Book Cover Design - Business/Self-Help Book

Book cover design for a business/self-help book. The title of the book is "OTTER Resolve - The Complete Blueprint for Triumph" It should also have "Harness the Seven Core Pillars Required for Triumph" as a subtitle somewhere.

Please see the website for an idea of the logo and sub-words: http://www.otterresolv.com

Book size will be 8.5" x 5.25"
Author info: Dorian Kebble

If your design includes a shark on the cover, it MUST be a hammerhead shark. Logo is attached.

I would like to stick with a red or orange theme like on the website but am open to any color idea. I like brighter colors and want the book to stand out and be attractive. If it's white, the wording and logo should be a bright color.

The back cover will just be preview text and selling points. It could have a picture in the background but will not have any pictures of the author.

If you include a spine design, please put the hammerhead logo on the spine.
Updates

Hello, The project description has been updated to include more details and preferences. The budget has also been increased. Thank you for your design! Added Thursday, December 31, 2015

Target Market(s)

Young Entrepreneurs and Business Professionals

Industry/Entity Type

Business

Requirements
Must have
• The hammerhead shark logo
Nice to have
• Look at the website - http://www.otterresolv.com
• It would be nice to have the six words throughout the cover similar to how it shows on the website cover picture.
Should not have
• Even though it caters to a younger crowd, it should not be cartoonish or child-like. Want a more serious and modern feel. Not too cluttered, i want the title to stand out and the shark to stand out.

```html
<!DOCTYPE html>
<html lang="en">
<head>
<meta charset="utf-8">
<title>Otter Resolve – Book Cover</title>
<link rel="stylesheet" href="https://fonts.googleapis.com/css2?family=Baloo+2:wght@800&family=Fredoka:wght@600&family=Ovo&display=swap">
<style>
  :root {
    --stage: #dfe5ea;
    --cover: #1b1b1b;
    --title-red: #d42a2a;
    --title-orange: #ea6a2a;
    --title-amber: #f2a23c;
    --title-cream: #f8dca0;
    --text-light: #f4f1ea;
    --art-orange: #e8602c;
    --art-amber: #d99a2e;
    --art-green: #3f6b45;
    --art-teal: #35594f;
  }
  * { margin: 0; padding: 0; box-sizing: border-box; }
  html, body {
    width: 1200px; height: 901px; overflow: hidden;
    background: var(--stage);
  }
  .book-cover {
    position: absolute; left: 321px; top: 0;
    width: 557px; height: 901px;
    background: var(--cover);
  }
  .title-block { position: absolute; left: 0; top: 0; width: 557px; height: 440px; }
  .title-line { font-family: "Baloo 2", "Arial Black", sans-serif; font-weight: 800; }
  .subtitle {
    font-family: "Fredoka", "Trebuchet MS", sans-serif; font-weight: 600;
    fill: var(--text-light);
  }
  .cover-art { position: absolute; left: 40px; top: 452px; width: 480px; height: 370px; }
  .author {
    position: absolute; left: 0; top: 818px; width: 557px;
    text-align: center;
    font-family: "Ovo", Georgia, serif; font-size: 27px;
    color: var(--text-light); letter-spacing: 0.5px;
  }
</style>
</head>
<body>
  <main class="book-cover">
    <svg class="title-block" viewBox="0 0 557 440" aria-label="OTTER Resolve – The Complete Blueprint for Triumph">
      <defs>
        <linearGradient id="title-fill" x1="0" y1="50" x2="0" y2="380" gradientUnits="userSpaceOnUse">
          <stop offset="0" stop-color="var(--title-red)"/>
          <stop offset="0.35" stop-color="var(--title-orange)"/>
          <stop offset="0.65" stop-color="var(--title-amber)"/>
          <stop offset="1" stop-color="var(--title-cream)"/>
        </linearGradient>
      </defs>
      <text class="title-line" x="40" y="160" font-size="128" fill="url(#title-fill)" textLength="472" lengthAdjust="spacingAndGlyphs">OTTER</text>
      <text class="title-line" x="40" y="280" font-size="128" fill="url(#title-fill)" textLength="472" lengthAdjust="spacingAndGlyphs">RESOLVE</text>
      <text class="title-line" x="40" y="326" font-size="40" fill="url(#title-fill)" textLength="472" lengthAdjust="spacingAndGlyphs">THE COMPLETE BLUEPRINT</text>
      <text class="title-line" x="40" y="380" font-size="62" fill="url(#title-fill)" textLength="472" lengthAdjust="spacingAndGlyphs">FOR TRIUMPH</text>
      <text class="subtitle" x="40" y="420" font-size="15" textLength="472" lengthAdjust="spacingAndGlyphs">Harness the Seven Core Pillars Required for Triumph</text>
    </svg>

    <svg class="cover-art" viewBox="0 0 480 370" role="img" aria-label="Illustration of a hammerhead shark swimming upward, coloured from orange-red at the head to green at the tail">
      <defs>
        <linearGradient id="art-fill" x1="0.7" y1="0" x2="0.2" y2="1">
          <stop offset="0" stop-color="var(--art-orange)"/>
          <stop offset="0.45" stop-color="var(--art-amber)"/>
          <stop offset="0.75" stop-color="var(--art-green)"/>
          <stop offset="1" stop-color="var(--art-teal)"/>
        </linearGradient>
      </defs>
      <ellipse cx="250" cy="190" rx="210" ry="150" fill="url(#art-fill)" opacity="0.85"/>
    </svg>

    <p class="author">Dorian Kebble</p>
  </main>
</body>
</html>
```